Fabrication and machining company needing printed material designs.

Heronfield Vessels, Inc. wants to use appealing visuals as well as informative text to tell potential clients about our capabilities in fabrication and machining. We have a new logo to showcase as well as a new website. The use of print media will allow us to leave tangible information with clients, and therefore the design will need to be concise, informative, and visually appealing.

Full Page Flyer (approx. 8.5" x 11"), front and back design. This will be a detailed offering of capabilities and services for our shop.

Half Page Flyer (approx. 5.5" x 8.5"), front and back design. An abbreviated version of the full page flyer, meant to be easily handed out and stored inside a note book.

Bi-fold business card front and back. General offerings of our services. Minimal if any details. Finished size is twice the size of a business card (approx. 4" x 3.5"), once folded in half will be the same size as a standard business card (approx. 2" x 3.5").

Please use www.heronfieldvesselsinc.example for theme ideas. The font used for our logo is ethnocentric, not to be used for all text.

Target Market(s)

Industrial Consumers

Font styles to use
Sans Serif

```html
<!DOCTYPE html>
<html lang="en">
<head>
<meta charset="utf-8">
<title>Heronfield Vessels, Inc. — Print Collateral</title>
<link rel="stylesheet" href="https://fonts.googleapis.com/css2?family=Montserrat:wght@400;600;700&family=Open+Sans:wght@400;600;700&family=Orbitron:wght@700&display=swap">
<style>
  :root{
    --stage:#2f2f2f;
    --slate:#4a4846;
    --slate-deep:#3e3c3a;
    --paper:#ececec;
    --white:#ffffff;
    --ink:#3a3a3a;
    --ink-soft:#555;
    --orange:#e8822a;
    --sky-top:#3f7fc4;
    --sky-low:#a9c7e6;
    --tank:#b9b6a4;
    --ground:#8a7f6a;
    --steel:#c9c9c9;
  }
  *{box-sizing:border-box;margin:0;padding:0}
  html,body{width:1093px;height:1200px;overflow:hidden;background:var(--stage)}
  body{position:relative;font-family:"Open Sans",Arial,sans-serif;color:var(--ink)}
  .piece{position:absolute;overflow:hidden;box-shadow:0 4px 14px rgba(0,0,0,.35)}
  .layer{position:absolute;inset:0;width:100%;height:100%}
  .abs{position:absolute}

  /* photo placeholders */
  .photo-tanks{position:absolute;background:
      linear-gradient(180deg,var(--sky-top) 0%,var(--sky-low) 45%,var(--tank) 46%,var(--tank) 80%,var(--ground) 81%,#6e6657 100%)}
  .photo-pipes{position:absolute;background:
      radial-gradient(ellipse 55% 40% at 55% 55%,var(--steel) 0%,#8e8e8e 45%,transparent 75%),
      linear-gradient(160deg,#5a5856 0%,var(--slate) 60%)}

  /* header block */
  .cert{position:absolute;font-family:"Montserrat",Arial,sans-serif;color:var(--ink);line-height:1.25}
  .cert b{display:block;font-weight:700}
  .cert small{display:block;font-weight:400}
  .brand{position:absolute;display:flex;align-items:center;gap:5px;color:var(--white);
         font-family:"Montserrat",Arial,sans-serif;font-weight:700;line-height:1.15;letter-spacing:.5px}
  .brand i{display:block;background:var(--white);flex:none}
  .contact{position:absolute;text-align:right;color:var(--white);font-family:"Montserrat",Arial,sans-serif;line-height:1.35}
  .contact strong{font-weight:700;display:block}

  /* specialities */
  .section-title{position:absolute;font-family:"Orbitron",Arial,sans-serif;font-weight:700;color:var(--orange);letter-spacing:1.5px}
  .spec-list{position:absolute;list-style:none;color:var(--white)}
  .spec-list li{position:absolute;white-space:nowrap}
  .spec-list li::before{content:"";display:inline-block;background:var(--orange);margin-right:6px;vertical-align:middle}

  /* equipment specs */
  .equip{position:absolute;text-align:center;font-family:"Montserrat",Arial,sans-serif}
  .equip h4{font-weight:700;color:var(--ink);letter-spacing:.4px;line-height:1.2}
  .equip p{color:var(--ink-soft);font-family:"Open Sans",Arial,sans-serif}

  /* services */
  .service-col{position:absolute;font-family:"Open Sans",Arial,sans-serif}
  .service-col h4{font-family:"Montserrat",Arial,sans-serif;color:var(--orange);font-weight:700;font-size:9.5px;letter-spacing:.6px;line-height:1.25}
  .service-col p{font-size:7.5px;line-height:1.42;color:var(--ink);margin:4px 0 0}

  .tagline{position:absolute;color:var(--white);font-family:"Montserrat",Arial,sans-serif;font-weight:700;letter-spacing:.5px}
  .intro{position:absolute;color:var(--white);font-weight:400}

  .about{position:absolute;color:var(--ink)}

  /* cards */
  .card{background:var(--slate);color:var(--white);font-family:"Montserrat",Arial,sans-serif}
  .card .stripe{position:absolute;left:0;right:0;height:5px;background:var(--orange)}
  .card .line{position:absolute;left:0;right:0;text-align:center}
  .icon{position:absolute}
</style>
</head>
<body>

<!-- ===== Full page flyer — front ===== -->
<section class="piece flyer-full-front" style="left:91px;top:56px;width:426px;height:551px;background:var(--slate)">
  <div class="photo-tanks" style="left:0;top:0;width:426px;height:272px;clip-path:polygon(0 0,100% 0,100% 87%,0 100%)" role="img" aria-label="Photo of large tan steel storage tanks with an access stairway under a blue sky"></div>
  <svg class="layer" viewBox="0 0 426 551" preserveAspectRatio="none" aria-hidden="true">
    <polygon points="0,0 130,0 58,112 0,112" fill="var(--white)"/>
    <polygon points="0,264 0,276 270,272 426,246 426,237" fill="var(--white)"/>
    <polygon points="300,370 426,352 426,364 330,372" fill="var(--orange)"/>
    <polygon points="0,382 426,362 426,551 0,551" fill="var(--paper)"/>
  </svg>
  <div class="cert" style="left:26px;top:22px;font-size:10.5px">
    <b>ISO 9001</b><b>API TANKS</b><small style="font-size:7px">12F, 620, 650</small><b style="margin-top:3px">AWWA</b>
  </div>
  <div class="brand" style="left:162px;top:24px;font-size:8px"><i style="width:18px;height:18px"></i><span>HERONFIELD<br>VESSELS, INC.</span></div>
  <div class="contact" style="right:28px;top:17px;font-size:7.5px">
    1450 West Route 12 Kestrel,<br>UT 84099
    <strong style="font-size:8.5px;margin-top:2px">T. (435) 555-0142</strong>
    <strong style="font-size:7px">www.heronfieldvesselsinc.example</strong>
  </div>
  <h2 class="section-title" style="left:26px;top:286px;font-size:12px">SPECIALITIES</h2>
  <ul class="spec-list" style="left:0;top:0;font-size:11.5px">
    <li style="left:26px;top:307px">Tanks</li>
    <li style="left:26px;top:323px">Piping</li>
    <li style="left:93px;top:307px">Firetubes</li>
    <li style="left:93px;top:323px">Pump Skids</li>
    <li style="left:190px;top:307px">Walkways &amp; Stairs</li>
    <li style="left:190px;top:323px">Trailer Components</li>
    <li style="left:330px;top:307px">Tank Vents</li>
    <li style="left:330px;top:323px">Clarifiers</li>
  </ul>
  <style>.flyer-full-front .spec-list li::before{width:4px;height:4px}
         .flyer-full-front .equip h4{font-size:9.5px}.flyer-full-front .equip p{font-size:7.5px;margin-top:2px}</style>
  <div class="equip" style="left:16px;top:392px;width:200px"><h4>HORIZONTAL LATHES:</h4><p>Up To 24" Dia &amp; 10' Long</p></div>
  <div class="equip" style="left:16px;top:428px;width:200px"><h4>VERTICAL LATHES:</h4><p>Up To 44" Dia</p></div>
  <div class="equip" style="left:16px;top:463px;width:200px"><h4>HORIZONTAL BORING<br>MILL CAPABILITIES</h4></div>
  <div class="equip" style="left:16px;top:499px;width:200px"><h4>PRESS BRAKE:</h4><p>1" Plate x 5' Wide, 3/8" Plate x 14' Wide</p></div>
  <div class="equip" style="left:207px;top:392px;width:200px"><h4>IRON WORKERS:</h4><p>Up To 85 Tons</p></div>
  <div class="equip" style="left:207px;top:432px;width:200px"><h4>BAND SOWS:</h4><p>22" Cut Capacity</p></div>
  <div class="equip" style="left:207px;top:467px;width:200px"><h4>CNC PLASMA CUTTING:</h4><p>8' x 20' Capacity</p></div>
  <div class="equip" style="left:207px;top:503px;width:200px"><h4>CNC POLL FORMING:</h4><p>1/2" x 10' Capacity</p></div>
</section>

<!-- ===== Full page flyer — back ===== -->
<section class="piece flyer-full-back" style="left:576px;top:56px;width:426px;height:551px;background:var(--paper)">
  <svg class="layer" viewBox="0 0 426 551" preserveAspectRatio="none" aria-hidden="true">
    <polygon points="0,0 426,0 426,322 0,338" fill="var(--slate)"/>
    <rect x="120" y="0" width="306" height="4" fill="var(--orange)"/>
    <polygon points="290,328 426,318 426,334 300,338" fill="var(--orange)"/>
  </svg>
  <div class="photo-pipes" style="left:0;top:4px;width:426px;height:240px" role="img" aria-label="Photo of a bent stainless steel pipe spool with welded flanges"></div>
  <svg class="layer" viewBox="0 0 426 551" preserveAspectRatio="none" aria-hidden="true">
    <polygon points="0,0 130,0 58,112 0,112" fill="var(--white)"/>
  </svg>
  <div class="cert" style="left:26px;top:22px;font-size:10.5px">
    <b>ISO 9001</b><b>API TANKS</b><small style="font-size:7px">12F, 620, 650</small><b style="margin-top:3px">AWWA</b>
  </div>
  <div class="brand" style="left:162px;top:24px;font-size:8px"><i style="width:18px;height:18px"></i><span>HERONFIELD<br>VESSELS, INC.</span></div>
  <div class="contact" style="right:28px;top:17px;font-size:7.5px">
    1450 West Route 12 Kestrel,<br>UT 84099
    <strong style="font-size:8.5px;margin-top:2px">T. (435) 555-0142</strong>
    <strong style="font-size:7px">www.heronfieldvesselsinc.example</strong>
  </div>
  <h2 class="tagline" style="left:41px;top:242px;font-size:12.5px">A BRILLIANT IDEA MATERIALIZED ...</h2>
  <p class="intro" style="left:41px;top:264px;font-size:11.5px;line-height:15.5px;width:380px">It is said great ideas start with a brilliant flash.<br>Likewise, we think a brilliant solution starts  with an arc.<br>From concept to construction we deliver results for the long haul.</p>

  <div class="service-col" style="left:57px;top:356px;width:95px">
    <h4>FACILITY</h4><p>35,000 ft2  Facility<br>5 Acre Storage Yard</p>
    <h4 style="margin-top:12px">DESIGN &amp;<br>ENGINEERING</h4><p>CAD Drawings<br>Engineering Services<br>3D Modeling</p>
    <h4 style="margin-top:12px">WELDING<br>PROCESSES</h4><p>Carbon Steel<br>Stainless Steel<br>Aluminum</p>
  </div>
  <div class="service-col" style="left:153px;top:356px;width:150px">
    <h4>PAINT &amp; CORROSION<br>CONTROL</h4><p>Dedicated Paint Bay<br>Plural Component Application Equip<br>Multi Step Liner Systems<br>Stainless Steel Passivation<br>Powder Coating<br>Galvanizing</p>
    <h4 style="margin-top:10px">SANDBLASTING</h4><p style="margin-top:6px">High Production Capacity</p>
    <h4 style="margin-top:11px">INSULATING SYSTEMS</h4><p>Polyurethane Spray Foam<br>Metal  Wrap<br>Heat Trace</p>
  </div>
  <div class="service-col" style="left:306px;top:356px;width:110px">
    <h4>HUDRAULIC<br>ASSEMBLES</h4><p>System Testing<br>Hose Assemblies<br>Ram Rebuilding</p>
    <h4 style="margin-top:12px">DRIVELINES</h4><p>Custom built<br>Rebuilding<br>Straightening</p>
  </div>
</section>

<!-- ===== Half page flyer — front ===== -->
<section class="piece flyer-half-front" style="left:91px;top:746px;width:268px;height:414px;background:var(--slate)">
  <div class="photo-tanks" style="left:0;top:0;width:268px;height:168px;clip-path:polygon(0 0,100% 0,100% 88%,0 100%)" role="img" aria-label="Photo of large tan steel storage tanks with an access stairway under a blue sky"></div>
  <svg class="layer" viewBox="0 0 268 414" preserveAspectRatio="none" aria-hidden="true">
    <polygon points="0,0 82,0 38,72 0,72" fill="var(--white)"/>
    <polygon points="0,164 0,172 170,170 268,152 268,147" fill="var(--white)"/>
    <polygon points="180,298 268,288 268,297 200,302" fill="var(--orange)"/>
    <polygon points="0,308 268,296 268,414 0,414" fill="var(--paper)"/>
  </svg>
  <div class="cert" style="left:16px;top:16px;font-size:7px">
    <b>ISO 9001</b><b>API TANKS</b><small style="font-size:5px">12F, 620, 650</small><b style="margin-top:3px">AWWA</b>
  </div>
  <div class="brand" style="left:96px;top:14px;font-size:5.5px"><i style="width:12px;height:12px"></i><span>HERONFIELD<br>VESSELS, INC.</span></div>
  <div class="contact" style="right:14px;top:10px;font-size:6px">
    1450 West Route 12 Kestrel,<br>UT 84099
    <strong style="font-size:6.5px;margin-top:1px">T. (435) 555-0142</strong>
    <strong style="font-size:5.3px">www.heronfieldvesselsinc.example</strong>
  </div>
  <h2 class="section-title" style="left:36px;top:199px;font-size:11px">SPECIALITIES</h2>
  <ul class="spec-list" style="left:0;top:0;font-size:10.5px">
    <li style="left:36px;top:215px">Tanks</li>
    <li style="left:36px;top:229px">Piping</li>
    <li style="left:36px;top:246px">Firetubes</li>
    <li style="left:36px;top:260px">Pump Skids</li>
    <li style="left:121px;top:215px">Walkways &amp; Stairs</li>
    <li style="left:121px;top:229px">Trailer Components</li>
    <li style="left:121px;top:246px">Tank Vents</li>
    <li style="left:121px;top:260px">Clarifiers</li>
  </ul>
  <style>.flyer-half-front .spec-list li::before{width:3px;height:3px}</style>
  <h2 class="section-title" style="left:36px;top:323px;font-size:11px">WHO WE ARE</h2>
  <p class="about" style="left:36px;top:341px;width:226px;font-size:10.5px;line-height:13.2px">Our world runs on natural and renewable resources. We are proud to make our livelihood supporting the industries that provide our quality of life.</p>
</section>

<!-- ===== Half page flyer — back ===== -->
<section class="piece flyer-half-back" style="left:413px;top:746px;width:268px;height:414px;background:var(--paper)">
  <svg class="layer" viewBox="0 0 268 414" preserveAspectRatio="none" aria-hidden="true">
    <polygon points="0,0 268,0 268,238 0,246" fill="var(--slate)"/>
    <rect x="70" y="0" width="198" height="3" fill="var(--orange)"/>
    <polygon points="190,241 268,234 268,246 200,247" fill="var(--orange)"/>
  </svg>
  <div class="photo-pipes" style="left:0;top:3px;width:268px;height:150px" role="img" aria-label="Photo of a bent stainless steel pipe spool with welded flanges"></div>
  <svg class="layer" viewBox="0 0 268 414" preserveAspectRatio="none" aria-hidden="true">
    <polygon points="0,0 82,0 38,72 0,72" fill="var(--white)"/>
  </svg>
  <div class="cert" style="left:11px;top:14px;font-size:7px">
    <b>ISO 9001</b><b>API TANKS</b><small style="font-size:5px">12F, 620, 650</small><b style="margin-top:3px">AWWA</b>
  </div>
  <div class="brand" style="left:94px;top:12px;font-size:5.5px"><i style="width:12px;height:12px"></i><span>HERONFIELD<br>VESSELS, INC.</span></div>
  <div class="contact" style="right:14px;top:8px;font-size:6px">
    1450 West Route 12 Kestrel,<br>UT 84099
    <strong style="font-size:6.5px;margin-top:1px">T. (435) 555-0142</strong>
    <strong style="font-size:5.3px">www.heronfieldvesselsinc.example</strong>
  </div>
  <h2 class="tagline" style="left:21px;top:164px;font-size:8px">A BRILLIANT IDEA MATERIALIZED ...</h2>
  <p class="intro" style="left:21px;top:180px;font-size:7px;line-height:9.6px;width:245px">It is said great ideas start with a brilliant flash.<br>Likewise, we think a brilliant solution starts  with an arc.<br>From concept to construction we deliver results for the long haul.</p>
  <style>.flyer-half-back .equip h4{font-size:7.5px}.flyer-half-back .equip p{font-size:5.8px;margin-top:2px;line-height:1.3}</style>
  <div class="equip" style="left:10px;top:268px;width:130px"><h4>HORIZONTAL LATHES:</h4><p>Up To 24" Dia &amp; 10' Long</p></div>
  <div class="equip" style="left:10px;top:298px;width:130px"><h4>VERTICAL LATHES:</h4><p>Up To 44" Dia</p></div>
  <div class="equip" style="left:10px;top:328px;width:130px"><h4>HORIZONTAL BORING<br>MILL CAPABILITIES</h4></div>
  <div class="equip" style="left:10px;top:362px;width:130px"><h4>PRESS BRAKE:</h4><p>1" Plate x 5' Wide,  3/8"<br>Plate x 14' Wide</p></div>
  <div class="equip" style="left:134px;top:268px;width:130px"><h4>IRON WORKERS:</h4><p>Up To 85 Tons</p></div>
  <div class="equip" style="left:134px;top:298px;width:130px"><h4>BAND SOWS:</h4><p>22" Cut Capacity</p></div>
  <div class="equip" style="left:134px;top:331px;width:130px"><h4>CNC PLASMA CUTTING:</h4><p>8' x 20' Capacity</p></div>
  <div class="equip" style="left:134px;top:361px;width:130px"><h4>CNC POLL FORMING:</h4><p>1/2" x 10' Capacity</p></div>
</section>

<!-- ===== Bi-fold card — outside ===== -->
<section class="piece card card-outside" style="left:771px;top:664px;width:205px;height:232px">
  <div class="line" style="top:12px;font-size:6px;transform:rotate(180deg)">www.heronfieldvesselsinc.example</div>
  <div class="stripe" style="top:114px"></div>
  <div class="brand" style="left:0;right:0;top:158px;justify-content:center;font-size:6.5px"><i style="width:12px;height:12px"></i><span>HERONFIELD<br>VESSELS, INC.</span></div>
</section>

<!-- ===== Bi-fold card — inside ===== -->
<section class="piece card card-inside" style="left:771px;top:927px;width:205px;height:232px">
  <div class="line" style="top:24px;font-size:9px;font-weight:700;line-height:12.5px">We specialize<br>in API-12F &amp; API-650 tank</div>
  <svg class="icon" style="left:96px;top:72px" width="13" height="13" viewBox="0 0 13 13" aria-hidden="true">
    <rect width="13" height="13" rx="2" fill="var(--white)"/>
    <path d="M6.5 2.2a3 3 0 0 0-3 3c0 2.2 3 5.6 3 5.6s3-3.4 3-5.6a3 3 0 0 0-3-3z" fill="var(--orange)"/>
    <circle cx="6.5" cy="5.2" r="1.1" fill="var(--white)"/>
  </svg>
  <div class="line" style="top:91px;font-size:7.5px;font-weight:400">1450 West Route 12 Kestrel, UT 84099</div>
  <div class="stripe" style="top:116px"></div>
  <svg class="icon" style="left:64px;top:181px" width="12" height="12" viewBox="0 0 12 12" aria-hidden="true">
    <rect width="12" height="12" rx="2" fill="var(--white)"/>
    <path d="M3.4 2.4l1.3-.2.8 1.9-.9.7c.4.9 1.1 1.6 2 2l.7-.9 1.9.8-.2 1.3c-3.2.2-5.8-2.4-5.6-5.6z" fill="var(--orange)"/>
  </svg>
  <div class="abs" style="left:82px;top:181px;font-size:7.5px">(435) 555-0142</div>
  <svg class="icon" style="left:40px;top:202px" width="12" height="12" viewBox="0 0 12 12" aria-hidden="true">
    <rect width="12" height="12" rx="2" fill="var(--white)"/>
    <circle cx="6" cy="6" r="3.6" fill="none" stroke="var(--orange)" stroke-width="1"/>
    <path d="M2.4 6h7.2M6 2.4c-1.6 2-1.6 5.2 0 7.2M6 2.4c1.6 2 1.6 5.2 0 7.2" fill="none" stroke="var(--orange)" stroke-width=".8"/>
  </svg>
  <div class="abs" style="left:58px;top:202px;font-size:7.5px">www.heronfieldvesselsinc.example</div>
</section>

</body>
</html>
```